Stationary and business card for an electrical contractor
Norvik Electric LLC
Stationary and business card for an electrical contractor - Construction
Creative Brief
Simple
Glen Hadley
President
412 N Orchard Ave
glen@norvikelectric-example.biz
WA Cont. # NORVIEL352TQ

```html
<!DOCTYPE html>
<html lang="en">
<head>
<meta charset="utf-8">
<title>Norvik Electric LLC – Stationery Set</title>
<link href="https://fonts.googleapis.com/css2?family=Montserrat:wght@400;600;800&family=Open+Sans:wght@400;600&display=swap" rel="stylesheet">
<style>
  :root {
    --red: #e3243b;
    --black: #111111;
    --paper: #ffffff;
    --ground: #eeeeee;
    --ink: #555555;
    --band: linear-gradient(to bottom, rgba(227,36,59,0) 0%, rgba(227,36,59,.55) 14%, #3a1418 34%, #111111 52%, #111111 100%);
  }
  * { margin: 0; padding: 0; box-sizing: border-box; }
  html, body { width: 1200px; height: 937px; overflow: hidden; }
  body { background: var(--ground); font-family: "Open Sans", sans-serif; position: relative; }

  .piece { position: absolute; background: var(--paper); overflow: hidden; box-shadow: 0 2px 6px rgba(0,0,0,.12); }
  .footer-band { position: absolute; left: 0; bottom: 0; width: 100%; background: var(--band); }

  .brand { font-family: "Montserrat", sans-serif; font-weight: 800; color: var(--black); text-transform: uppercase; line-height: .95; display: flex; align-items: center; gap: 6px; }
  .brand .dot { width: 10px; height: 10px; background: var(--red); flex: none; }
  .brand .name { display: block; }

  /* Letterhead */
  .letterhead { left: 182px; top: 66px; width: 390px; height: 544px; }
  .letterhead .brand { position: absolute; left: 34px; top: 30px; font-size: 15px; }
  .letterhead .footer-band { height: 165px; }
  .letter-body { position: absolute; left: 34px; top: 100px; width: 300px; font-size: 4.6px; line-height: 1.55; color: var(--ink); }
  .letter-body p { margin-bottom: 7px; }
  .letter-body .sign-space { height: 22px; }
  .letter-footer { position: absolute; right: 26px; bottom: 18px; text-align: right; font-size: 4.4px; line-height: 1.6; color: #fff; }

  /* Second sheet */
  .sheet { left: 635px; top: 40px; width: 393px; height: 570px; }
  .sheet .brand { position: absolute; left: 50%; top: 210px; transform: translateX(-50%); font-size: 40px; gap: 12px; }
  .sheet .brand .dot { width: 22px; height: 22px; }
  .sheet .footer-band { height: 175px; }
  .sheet .web { position: absolute; right: 26px; bottom: 16px; font-family: "Montserrat", sans-serif; font-size: 7px; letter-spacing: 1.6px; color: #fff; }

  /* Business cards */
  .card { left: 46px; width: 197px; height: 90px; border-radius: 3px; }
  .card-front { top: 737px; }
  .card-front .brand { position: absolute; left: 12px; top: 14px; font-size: 11px; }
  .card-front .brand .dot { width: 7px; height: 7px; }
  .card-front .footer-band { height: 40px; }
  .card-contact { position: absolute; left: 100px; top: 12px; font-size: 4.3px; line-height: 1.55; color: var(--ink); }
  .card-contact strong { font-family: "Montserrat", sans-serif; font-weight: 600; color: var(--black); font-size: 5px; }
  .card-back { top: 838px; background: var(--black); }
  .card-back .brand { position: absolute; left: 16px; top: 30px; font-size: 14px; color: #fff; }

  /* Envelope front */
  .envelope { left: 266px; top: 747px; width: 430px; height: 164px; }
  .envelope .brand { position: absolute; left: 20px; top: 18px; font-size: 15px; }
  .envelope .footer-band { height: 92px; }
  .envelope .web { position: absolute; right: 24px; bottom: 10px; font-family: "Montserrat", sans-serif; font-size: 6.5px; letter-spacing: 1.5px; color: #fff; }

  /* Envelope back */
  .envelope-back { left: 734px; top: 742px; width: 425px; height: 169px; }
  .envelope-back .flap { position: absolute; left: 0; top: 0; width: 100%; height: 100px; display: block; }
  .envelope-back .web { position: absolute; left: 0; width: 100%; top: 56px; text-align: center; font-family: "Montserrat", sans-serif; font-size: 6.5px; letter-spacing: 1.5px; color: #fff; }
</style>
</head>
<body>

<article class="piece letterhead">
  <div class="brand"><span class="dot"></span><span class="name">Norvik<br>Electric</span></div>
  <div class="letter-body">
    <p>July 3, 2024<br>Dana Reyes<br>Harbor Build Co.<br>210 Pine St, Tacoma, WA</p>
    <p>We are pleased to confirm our electrical work on your project. Our crew will begin the panel upgrade and wiring next week, following the approved plans and local code requirements. Please let us know of any site access details before we start.</p>
    <p>All materials are covered by our standard warranty, and every job is inspected before final sign off.</p>
    <p>Thank you for choosing us. We look forward to working with you.</p>
    <p>Sincerely,</p>
    <div class="sign-space"></div>
    <p>Glen Hadley<br>President<br>412 N Orchard Ave</p>
  </div>
  <div class="footer-band" role="img" aria-label="Decorative red and black swoosh footer"></div>
  <div class="letter-footer">
    412 N Orchard Ave<br>Tacoma, WA 98402<br>(253) 555-0148<br>glen@norvikelectric-example.biz<br>www.norvikelectric-example.biz<br>WA Cont. # NORVIEL352TQ
  </div>
</article>

<article class="piece sheet">
  <div class="brand"><span class="dot"></span><span class="name">Norvik<br>Electric</span></div>
  <div class="footer-band" role="img" aria-label="Decorative red and black swoosh footer"></div>
  <div class="web">www.norvikelectric-example.biz</div>
</article>

<article class="piece card card-front">
  <div class="brand"><span class="dot"></span><span class="name">Norvik<br>Electric</span></div>
  <div class="card-contact">
    <strong>Glen Hadley</strong><br>President<br>(253) 555-0148<br>glen@norvikelectric-example.biz<br>412 N Orchard Ave<br>Tacoma, WA 98402
  </div>
  <div class="footer-band" role="img" aria-label="Decorative red and black swoosh footer"></div>
</article>

<article class="piece card card-back">
  <div class="brand"><span class="name">Norvik<br>Electric</span></div>
</article>

<article class="piece envelope">
  <div class="brand"><span class="dot"></span><span class="name">Norvik<br>Electric</span></div>
  <div class="footer-band" role="img" aria-label="Decorative red and black swoosh footer"></div>
  <div class="web">www.norvikelectric-example.biz</div>
</article>

<article class="piece envelope-back">
  <svg class="flap" viewBox="0 0 425 100" preserveAspectRatio="none">
    <path d="M0 0 H425 V70 C330 80 250 96 212 96 C174 96 95 80 0 70Z" fill="#111111"/>
  </svg>
  <div class="web">www.norvikelectric-example.biz</div>
</article>

</body>
</html>
```